Solar appointment reminder card

We are looking for a new design for our appointment reminder card since we have changed our logo. The card should have the new logo along with space for the employee to hand write the customers appointment date, time, the employees name and phone number.
I've uploaded what our old basic appointment card looked like and our new logo.

The cards should be in a standard business card size and could be horizontal or vertical.

```html
<!DOCTYPE html>
<html lang="en">
<head>
<meta charset="utf-8">
<title>Sunvale Solar – Appointment Card</title>
<link rel="stylesheet" href="https://fonts.googleapis.com/css2?family=Lexend:wght@400;500;700&display=swap">
<style>
  :root {
    --card-green: #16624e;
    --sun-yellow: #ffc513;
    --brand-orange: #f47b0b;
  }
  html, body {
    margin: 0;
    padding: 0;
    overflow: hidden;
    background: var(--card-green);
  }
  .card {
    position: relative;
    width: 686px;
    height: 1200px;
    background: var(--card-green);
    font-family: "Lexend", sans-serif;
    color: var(--sun-yellow);
    overflow: hidden;
  }
  .brand {
    position: absolute;
    left: 44px;
    top: 372px;
    width: 600px;
    height: 240px;
    display: flex;
    align-items: center;
    gap: 36px;
  }
  .brand-dot {
    flex: 0 0 auto;
    width: 180px;
    height: 180px;
    border-radius: 50%;
    background: var(--sun-yellow);
  }
  .brand-name {
    margin: 0;
    font-size: 78px;
    font-weight: 700;
    line-height: 1;
    color: var(--brand-orange);
    letter-spacing: 1px;
  }
  .card-title,
  .card-role,
  .contact {
    position: absolute;
    left: 0;
    right: 0;
    margin: 0;
    text-align: center;
    font-style: normal;
  }
  .card-title {
    top: 713px;
    font-size: 55px;
    font-weight: 400;
    line-height: 66px;
  }
  .card-role {
    top: 775px;
    font-size: 48px;
    font-weight: 400;
    line-height: 58px;
  }
  .contact {
    top: 853px;
    font-size: 31px;
    font-weight: 500;
    line-height: 33px;
  }
  .appointment-fields {
    position: absolute;
    left: 104px;
    right: 104px;
    top: 950px;
    margin: 0;
    padding: 0;
    list-style: none;
  }
  .field {
    display: flex;
    align-items: flex-end;
    gap: 14px;
    height: 48px;
    font-size: 24px;
    font-weight: 400;
    line-height: 1;
  }
  .field-label {
    flex: 0 0 92px;
  }
  .field-line {
    flex: 1 1 auto;
    height: 0;
    border-bottom: 2px solid var(--sun-yellow);
    margin-bottom: 3px;
  }
</style>
</head>
<body>
  <main class="card">
    <header class="brand">
      <span class="brand-dot" aria-hidden="true"></span>
      <h1 class="brand-name">Sunvale<br>Solar</h1>
    </header>
    <h2 class="card-title">Appointment Card</h2>
    <p class="card-role">CEO</p>
    <address class="contact">
      42 Orchard Ln, Albany<br>
      +1 555 0147
    </address>
    <ul class="appointment-fields">
      <li class="field"><span class="field-label">Date</span><span class="field-line"></span></li>
      <li class="field"><span class="field-label">Time</span><span class="field-line"></span></li>
      <li class="field"><span class="field-label">Name</span><span class="field-line"></span></li>
      <li class="field"><span class="field-label">Phone</span><span class="field-line"></span></li>
    </ul>
  </main>
</body>
</html>
```